New eyelid plastic surgery office needs a business card design-Eyelid Surgery Partners of Brennor

I recently used SketchHarbor for my logo design and was very pleased with creativity and results. It was a difficult decision for me. Now I would like to create a business card based on this logo, which I will attach.

The text should be easily legible as some of my patients have difficulty seeing, but I would like a subtle, sophisticated artistry also evident to make the card memorable. Would like the card based on a similar color scheme as the logo but the inverse or other complementary colors may prove interesting

A good question was asked...my concern about my visually impaired patients was really my desire to avoid italicized or calligraphic type fonts that may be hard to read. Standard font size for a business card would be fine. Thanks!

Thank you so much for the great work so far. I wanted to give you my particular contact information to see if that would change the look of the cards. Martin Pellowby, MD Address: 2817 Larkmoor Avenue, Suite 205 Wilmington, NC 28517 Phone: 910-555-0183 Fax: 910-555-0184 Website: www.brennorlidclinic.example Please delete the email slot from the card. Thanks so much!

Reason: Last minute consideration. So many great revisions right now!

Plastic

```html
<!DOCTYPE html>
<html lang="en">
<head>
<meta charset="utf-8">
<title>Eyelid Surgery Partners of Brennor – Business Card</title>
<link rel="stylesheet" href="https://fonts.googleapis.com/css2?family=Montserrat:wght@300;400;500&display=swap">
<style>
  :root {
    --page-bg: #e9ebee;
    --card-white: #ffffff;
    --card-edge: #d6d9de;
    --blue-deep: #0a4fc0;
    --blue-mid: #1a7fe6;
    --blue-light: #3ca6f4;
    --swoosh-grey: #8f959c;
    --swoosh-grey-light: #c7cbd0;
    --brand-blue: #1f4e9e;
    --text-on-blue: #ffffff;
  }
  * { box-sizing: border-box; margin: 0; padding: 0; }
  html, body {
    width: 1200px; height: 900px; overflow: hidden;
    background: var(--page-bg);
    font-family: "Montserrat", Arial, sans-serif;
  }
  .sheet {
    position: relative; width: 1200px; height: 900px;
    display: flex; align-items: center; justify-content: center; gap: 60px;
  }
  .card {
    position: relative; width: 540px; height: 310px;
    border-radius: 22px; overflow: hidden;
    background: var(--card-white);
    box-shadow: 0 2px 0 var(--card-edge), 0 14px 30px rgba(30, 40, 60, 0.16);
  }
  .card-shapes { position: absolute; inset: 0; width: 100%; height: 100%; }

  .brand-name {
    position: absolute;
    color: var(--brand-blue);
    font-weight: 400;
    text-transform: uppercase;
    letter-spacing: 0.04em;
    line-height: 1.15;
  }
  .card-front .brand-name { left: 22px; top: 62px; width: 270px; font-size: 19px; }
  .card-back .brand-name {
    left: 0; right: 0; top: 50%; transform: translateY(-50%);
    text-align: center; font-size: 28px; padding: 0 40px;
  }

  .contact {
    position: absolute; right: 26px; top: 58px;
    text-align: right; color: var(--text-on-blue);
  }
  .contact-name { font-size: 15px; font-weight: 500; letter-spacing: 0.06em; text-transform: uppercase; }
  .contact-role { font-size: 11px; font-weight: 300; margin-top: 3px; }
  .contact-address { font-size: 11px; font-weight: 300; line-height: 1.5; margin-top: 18px; }
  .contact-lines { list-style: none; margin-top: 24px; }
  .contact-lines li {
    display: flex; justify-content: flex-end; align-items: center; gap: 8px;
    font-size: 11px; font-weight: 300; line-height: 1.95;
  }
  .contact-lines svg { width: 11px; height: 11px; flex: none; }
</style>
</head>
<body>
<main class="sheet">

  <section class="card card-front" aria-label="Business card front">
    <svg class="card-shapes" viewBox="0 0 540 310" preserveAspectRatio="none" aria-hidden="true">
      <defs>
        <radialGradient id="blueField" cx="0.55" cy="0.6" r="0.8">
          <stop offset="0" stop-color="var(--blue-light)"/>
          <stop offset="0.55" stop-color="var(--blue-mid)"/>
          <stop offset="1" stop-color="var(--blue-deep)"/>
        </radialGradient>
        <linearGradient id="swooshShade" x1="0" y1="0" x2="1" y2="1">
          <stop offset="0" stop-color="var(--swoosh-grey-light)"/>
          <stop offset="1" stop-color="var(--swoosh-grey)"/>
        </linearGradient>
      </defs>
      <rect width="540" height="310" fill="url(#blueField)"/>
      <path d="M0 0 H352 C324 138 196 226 0 238 Z" fill="url(#swooshShade)"/>
      <path d="M0 0 H330 C300 122 180 198 0 212 Z" fill="var(--card-white)"/>
    </svg>

    <div class="brand-name">Eyelid Surgery Partners of Brennor</div>

    <div class="contact">
      <div class="contact-name">Daniel Whitcombe</div>
      <div class="contact-role">Managing Director</div>
      <div class="contact-address">412, 6th Floor, Harbor Point<br>Quarry Lane WLM</div>
      <ul class="contact-lines">
        <li>012 555 0147
          <svg viewBox="0 0 12 12" aria-hidden="true"><path d="M2.5 1 L4.5 1 L5.3 3.4 L4 4.4 C4.7 5.9 6.1 7.3 7.6 8 L8.6 6.7 L11 7.5 L11 9.5 C11 10.3 10.3 11 9.5 11 C5 11 1 7 1 2.5 C1 1.7 1.7 1 2.5 1 Z" fill="currentColor"/></svg>
        </li>
        <li>012 555 0148
          <svg viewBox="0 0 12 12" aria-hidden="true"><rect x="3" y="0.5" width="6" height="11" rx="1.2" fill="none" stroke="currentColor"/><circle cx="6" cy="9.6" r="0.7" fill="currentColor"/></svg>
        </li>
        <li>hello@brennorlid.example
          <svg viewBox="0 0 12 12" aria-hidden="true"><rect x="0.5" y="2.5" width="11" height="7" fill="currentColor"/><path d="M0.8 2.8 L6 6.6 L11.2 2.8" fill="none" stroke="var(--blue-mid)" stroke-width="0.9"/></svg>
        </li>
        <li>www.brennorlid.example
          <svg viewBox="0 0 12 12" aria-hidden="true"><circle cx="6" cy="6" r="5" fill="none" stroke="currentColor"/><ellipse cx="6" cy="6" rx="2.2" ry="5" fill="none" stroke="currentColor" stroke-width="0.8"/><path d="M1 6 H11" stroke="currentColor" stroke-width="0.8"/></svg>
        </li>
      </ul>
    </div>
  </section>

  <section class="card card-back" aria-label="Business card back">
    <div class="brand-name">Eyelid Surgery Partners of Brennor</div>
  </section>

</main>
</body>
</html>
```